ONE TRUE PACE Personal Training Website.

I am looking for a website design for Word Press URL I already have. I have it as 10 very simple pages. Once home page design is set we can use that look on all other pages. I have uploaded a word document that has an outline of what I am looking for. Please take the time to review this. I want to add this is for a WordPress site.

Target Market(s)

Women 25-55

Industry/Entity Type

Health And Wellness

Coding

Coded - Design and coding required

Number of Pages Required

5+ page

```html
<!DOCTYPE html>
<html lang="en">
<head>
<meta charset="utf-8">
<title>ONE TRUE PACE – Personal Training</title>
<link rel="stylesheet" href="https://fonts.googleapis.com/css2?family=Montserrat:wght@400;500;600;700&family=Open+Sans:wght@400;600&family=Tinos:ital,wght@0,400;1,400&family=Arimo:wght@700&family=Playfair+Display:ital,wght@1,700&display=swap">
<style>
:root{
  --red:#c8202e;
  --teal:#1f9a8c;
  --ink:#2b2b2b;
  --muted:#777;
  --page:#ffffff;
  --soft:#f3f3f3;
  --dark:#1c1c1c;
  --veil:rgba(25,25,25,.46);
}
*{box-sizing:border-box;margin:0;padding:0}
html,body{width:1200px;height:3965px;overflow:hidden}
body{position:relative;background:var(--page);font-family:"Open Sans",Arial,sans-serif;color:var(--ink)}
.abs{position:absolute}
h2.section-title{position:absolute;left:0;width:1200px;text-align:center;font-family:"Montserrat",sans-serif;font-weight:600;font-size:30px;color:var(--ink)}
.section-sub{position:absolute;left:0;width:1200px;text-align:center;font-size:13px;color:var(--muted)}
.btn-outline{position:absolute;height:34px;border:2px solid var(--red);border-radius:17px;font-family:"Montserrat",sans-serif;font-size:11px;font-weight:600;color:var(--red);display:flex;align-items:center;justify-content:center}
.photo{position:absolute}

/* hero */
.hero{position:absolute;left:0;top:0;width:1200px;height:568px;background:radial-gradient(circle at 30% 60%,#6a6a6a,#2c2c2c 70%)}
.brand{position:absolute;left:72px;top:30px;display:flex;align-items:center;gap:12px;font-family:"Montserrat",sans-serif;font-weight:700;font-size:18px;color:#fff}
.brand-dot{width:50px;height:50px;border-radius:50%;background:var(--red)}
.nav{position:absolute;left:312px;top:50px;display:flex;gap:30px;font-family:"Montserrat",sans-serif;font-size:13px;color:#fff}
.nav .active{color:var(--teal)}
.nav-signup{position:absolute;left:1018px;top:40px;width:113px;height:38px;border-radius:19px;background:var(--red);color:#fff;font-family:"Montserrat",sans-serif;font-size:12px;font-weight:600;display:flex;align-items:center;justify-content:center}
.follow{position:absolute;left:70px;top:260px;width:20px;display:flex;flex-direction:column;align-items:center;gap:10px}
.follow span{width:12px;height:12px;border:1.5px solid #fff;border-radius:2px}
.follow em{font-style:normal;color:#fff;font-size:10px;writing-mode:vertical-rl;transform:rotate(180deg);margin-top:6px}
.hero-quote{position:absolute;left:0;top:222px;width:1200px;text-align:center;color:#fff;font-family:"Montserrat",sans-serif;font-weight:700;font-size:40px}
.hero-quote-2{position:absolute;left:0;top:278px;width:1200px;text-align:center;color:#fff;font-family:"Playfair Display",serif;font-style:italic;font-size:30px}
.hero-btn{position:absolute;left:503px;top:348px;width:194px;height:36px;border:2px solid #fff;border-radius:18px;color:#fff;font-family:"Montserrat",sans-serif;font-size:12px;display:flex;align-items:center;justify-content:center}
.hero-btn b{color:var(--teal);font-weight:500;margin-left:4px}
.dots{position:absolute;left:1116px;top:262px;display:flex;flex-direction:column;gap:12px}
.dots span{width:10px;height:10px;border:1.5px solid #fff;border-radius:50%}

/* about */
.about{position:absolute;left:0;top:568px;width:1200px;height:450px;background:var(--soft);overflow:hidden}
.about-title{position:absolute;left:206px;top:62px;font-family:"Montserrat",sans-serif;font-weight:600;font-size:28px}
.about-lead{position:absolute;left:206px;top:108px;font-family:"Montserrat",sans-serif;font-weight:600;font-size:14px;color:var(--teal)}
.about-text{position:absolute;left:206px;width:490px;font-size:11.5px;line-height:17px;color:var(--muted)}

/* certification */
.cert-card{position:absolute;top:1163px;width:336px;height:198px;background:linear-gradient(#f4f2ec,#e6e3da);border:1px solid #ddd}
.cert-label{position:absolute;top:1376px;width:336px;text-align:center;font-family:"Montserrat",sans-serif;font-weight:600;font-size:13px;line-height:18px}
.arrow{position:absolute;font-size:20px;color:#888}

/* blog */
.blog-band{position:absolute;left:0;top:2088px;width:410px;height:428px;background:var(--teal)}
.blog-card{position:absolute;left:410px;top:2300px;width:396px;height:216px;background:#fff;padding:22px 46px}
.blog-card h4{font-family:"Montserrat",sans-serif;font-size:13px;line-height:18px;margin-bottom:12px}
.blog-card p{font-size:11px;line-height:16px;color:var(--muted)}
.blog-card a{display:block;margin-top:12px;font-family:"Montserrat",sans-serif;font-size:10px;font-weight:600;color:var(--red)}

/* training */
.train-card{position:absolute;top:2669px;width:248px;height:178px;border-radius:6px;overflow:hidden}
.train-card .num{position:absolute;left:18px;bottom:30px;color:#fff;font-family:"Montserrat",sans-serif;font-weight:700;font-size:22px}
.train-card .name{position:absolute;left:18px;bottom:12px;color:#fff;font-family:"Montserrat",sans-serif;font-size:13px}

/* testimonials */
.testi{position:absolute;left:71px;top:2981px;width:1057px;height:381px;background:linear-gradient(#4a4a4a,#2f2f2f)}
.testi-text{position:absolute;left:150px;top:120px;width:757px;text-align:center;color:#fff;font-size:13px;line-height:20px}

/* contact */
.field{position:absolute;width:370px;border-bottom:1px solid #ccc;padding-bottom:10px;font-size:10px;color:var(--muted);letter-spacing:.5px}

/* footer */
.footer{position:absolute;left:0;top:3785px;width:1200px;height:180px;background:var(--dark)}
.footer-icons{position:absolute;left:562px;top:60px;display:flex;gap:12px}
.footer-icons span{width:32px;height:32px;border-radius:50%;border:2px solid #fff}
.footer-icons span.on{background:var(--red);border-color:var(--red)}
.footer-copy{position:absolute;left:0;top:108px;width:1200px;text-align:center;color:#aaa;font-size:11px}
.footer-copy b{color:var(--red);font-weight:600}

/* dimming veil and certificate window */
.veil{position:absolute;left:0;top:0;width:1200px;height:3965px;background:var(--veil)}
.cert-window{position:absolute;left:211px;top:1683px;width:783px;height:595px;background:#fff;border:3px solid #e9e9e9;box-shadow:0 0 30px rgba(0,0,0,.35);font-family:"Tinos",serif;text-align:center;color:#111}
.cert-window .org{position:absolute;left:0;top:44px;width:100%;font-size:36px}
.cert-window .line{position:absolute;left:0;width:100%;font-style:italic;font-size:25px}
.cert-window .bold{position:absolute;left:0;width:100%;font-family:"Arimo",sans-serif;font-weight:700;font-size:19px}
.cert-number{position:absolute;left:302px;top:348px;width:180px;border-bottom:1.5px solid #111;font-family:"Arimo",sans-serif;font-weight:700;font-size:17px}
.cert-caption{position:absolute;left:302px;top:378px;width:180px;font-style:italic;font-size:15px}
.cert-brand{position:absolute;left:30px;top:478px;display:flex;align-items:center;gap:10px;font-family:"Arimo",sans-serif;font-weight:700;font-size:30px;color:#1d2b5c}
.cert-brand i{width:26px;height:26px;background:#1d2b5c}
.cert-sign{position:absolute;left:520px;top:470px;width:230px;height:46px}
.cert-role{position:absolute;left:500px;top:528px;width:265px;border-top:1.5px solid #111;font-style:italic;font-size:14px;padding-top:4px}
.close-btn{position:absolute;left:966px;top:1663px;width:40px;height:40px;border-radius:50%;background:var(--red);border:3px solid #fff}
</style>
</head>
<body>

<!-- hero -->
<section class="hero">
  <div class="photo" role="img" aria-label="Black and white close-up of a kettlebell in a gym" style="inset:0;background:radial-gradient(ellipse at 25% 70%,#7a7a7a,#333 65%)"></div>
  <div class="brand"><span class="brand-dot"></span>ONE TRUE PACE</div>
  <nav class="nav"><span class="active">Home</span><span>Certifications</span><span>Bio</span><span>Blog</span><span>Videos</span><span>Online Training</span><span>Nutrition</span><span>Merchandise</span><span>Contact Us</span></nav>
  <div class="nav-signup">Sign Up!</div>
  <div class="follow"><span></span><span></span><em>Follow Us</em></div>
  <h1 class="hero-quote">“If it doesn’t Challenge you,</h1>
  <p class="hero-quote-2">it won’t Change you”</p>
  <div class="hero-btn">Sign Up For <b>Your Goal</b></div>
  <div class="dots"><span></span><span></span><span></span><span></span><span></span></div>
  <svg class="abs" style="left:592px;top:518px" width="16" height="10"><path d="M2 2l6 6 6-6" stroke="#fff" stroke-width="1.6" fill="none"/></svg>
</section>

<!-- about -->
<section class="about">
  <svg class="abs" style="left:830px;top:0" width="370" height="450"><polygon points="150,0 370,0 370,450 0,450" fill="var(--teal)"/></svg>
  <h2 class="about-title">About Us</h2>
  <p class="about-lead">There are many variations of passages Ipsum available.</p>
  <p class="about-text" style="top:130px">Contrary to popular belief, Lorem Ipsum is not simply random text. It has roots in a piece of classical Latin literature from 45 BC, making it over 2000 years old. A Latin professor in Virginia looked up one of the more obscure Latin words, consectetur, from a Lorem ...</p>
  <p class="about-text" style="top:210px">There are many variations of passages of Lorem Ipsum available, but the majority have suffered alteration in some form, by injected humour, or randomised words which don't look even slightly believable ...</p>
  <div class="btn-outline" style="left:206px;top:340px;width:126px">Discover More</div>
  <div class="photo" role="img" aria-label="Woman in a visor running a race" style="left:745px;top:72px;width:383px;height:304px;background:linear-gradient(120deg,#5d6b74,#b8876f 55%,#3e4a52)"></div>
</section>

<!-- certification -->
<h2 class="section-title" style="top:1078px">NIMS certification</h2>
<p class="section-sub" style="top:1122px">There are many variations of passages of Lorem Ipsum available</p>
<div class="arrow" style="left:158px;top:1248px">‹</div>
<div class="arrow" style="left:1030px;top:1248px">›</div>
<div class="cert-card" role="img" aria-label="Corrective Exercise Specialist certificate" style="left:206px"></div>
<div class="cert-card" role="img" aria-label="Fitness Nutrition Specialist certificate" style="left:476px"></div>
<div class="cert-card" role="img" aria-label="Certified Personal Trainer certificate" style="left:745px"></div>
<p class="cert-label" style="left:206px">Corrective Exercise<br>Specialist</p>
<p class="cert-label" style="left:476px">Fitness Nutrition Specialist<br>(FNS)</p>
<p class="cert-label" style="left:745px">Certified Personal<br>Trainer</p>
<div class="btn-outline" style="left:537px;top:1440px;width:126px">View All</div>

<!-- videos -->
<h2 class="section-title" style="top:1606px">Videos</h2>
<p class="section-sub" style="top:1650px">There are many variations of passages of Lorem</p>
<div class="photo" role="img" aria-label="Training video thumbnails" style="left:206px;top:1690px;width:790px;height:360px;background:linear-gradient(#888,#555)"></div>

<!-- blog -->
<section>
  <div class="blog-band"></div>
  <h2 class="abs" style="left:71px;top:2218px;font-family:'Montserrat',sans-serif;font-weight:600;font-size:28px;color:#fff">Latest Blog</h2>
  <p class="abs" style="left:71px;top:2262px;width:200px;font-size:11px;line-height:15px;color:#e8f5f3">At vero eos et accusamus et iusto odio dignissimos ducimus qui blanditiis praesentium voluptatum.</p>
  <div class="btn-outline" style="left:71px;top:2350px;width:110px;border-color:#fff;color:#fff">View All Blog</div>
  <div class="blog-card" style="top:2100px;left:410px;width:720px;height:190px;background:#fff">
    <h4 style="margin-left:400px">Contrary to popular belief, Lorem Ipsum is not simply random text.</h4>
    <p style="margin-left:400px">There are many variations of passages of Lorem Ipsum available, but the majority have suffered alteration in some form, by injected humour ...</p>
  </div>
  <div class="blog-card">
    <h4>Contrary to popular belief, Lorem Ipsum is not simply random text.</h4>
    <p>There are many variations of passages of Lorem Ipsum available, but the majority have suffered alteration in some form, by injected humour, or randomised...</p>
    <a>+ Explore More</a>
  </div>
  <div class="photo" role="img" aria-label="Weight plates and a barbell on a gym floor" style="left:806px;top:2300px;width:322px;height:216px;background:linear-gradient(135deg,#8a8a8a,#3a3a3a)"></div>
</section>

<!-- online training -->
<h2 class="section-title" style="top:2581px">Online Training</h2>
<p class="section-sub" style="top:2622px">But I must explain to you how all this mistaken idea of denouncing</p>
<div class="arrow" style="left:158px;top:2740px">‹</div>
<div class="arrow" style="left:1030px;top:2740px">›</div>
<div class="train-card" role="img" aria-label="Woman training with a resistance rope" style="left:206px;background:linear-gradient(135deg,#c9b0a6,#7a6a66)"><span class="num">01</span><span class="name">Weight Loss</span></div>
<div class="train-card" role="img" aria-label="Man lifting a dumbbell" style="left:476px;background:linear-gradient(135deg,#555,#222)"><span class="num">02</span><span class="name">Body Building</span></div>
<div class="train-card" role="img" aria-label="Group stretching in a studio" style="left:745px;background:linear-gradient(135deg,#8a5a5a,#3a2a2a)"><span class="num">03</span><span class="name">Stretching</span></div>
<div class="btn-outline" style="left:537px;top:2875px;width:126px">View All Training</div>

<!-- testimonials -->
<section class="testi">
  <h2 class="abs" style="left:0;top:70px;width:1057px;text-align:center;font-family:'Montserrat',sans-serif;font-weight:600;font-size:30px;color:#fff">Testimonials</h2>
  <p class="abs" style="left:0;top:108px;width:1057px;text-align:center;color:var(--red);font-size:28px;font-family:'Tinos',serif">“</p>
  <p class="testi-text" style="top:138px">I wasn't sure if Marisa was interested in training my then 11-year-old daughter, but after talking with her she was 100% committed to what we wanted to accomplish with our daughter. After their first intro session together, my daughter was excited and nervous about this new journey of training ...</p>
  <p class="abs" style="left:0;top:240px;width:1057px;text-align:center;color:var(--teal);font-family:'Montserrat',sans-serif;font-weight:600;font-size:15px">Jenna</p>
  <p class="abs" style="left:0;top:262px;width:1057px;text-align:center;color:#ccc;font-size:11px">Pine Ridge CO</p>
  <div class="abs" style="left:895px;top:170px;display:flex;flex-direction:column;gap:10px"><span style="width:8px;height:8px;border:1.5px solid #fff;border-radius:50%"></span><span style="width:8px;height:8px;background:#fff;border-radius:50%"></span></div>
</section>

<!-- contact -->
<h2 class="section-title" style="top:3422px">Contact Us</h2>
<p class="section-sub" style="top:3463px">We are here to help you 24 hours a day</p>
<div class="field" style="left:283px;top:3510px">NAME</div>
<div class="field" style="left:617px;top:3510px;width:300px">EMAIL</div>
<div class="field" style="left:283px;top:3566px">PHONE</div>
<div class="field" style="left:617px;top:3566px;width:300px">ADDRESS</div>
<div class="field" style="left:283px;top:3622px;width:634px">COMMENTS</div>
<div class="btn-outline" style="left:553px;top:3679px;width:94px">Send</div>

<!-- footer -->
<footer class="footer">
  <div class="footer-icons"><span></span><span class="on"></span></div>
  <p class="footer-copy">© 2018 <b>ONE TRUE PACE</b>. All Rights Reserved.</p>
</footer>

<!-- dimming veil with certificate window -->
<div class="veil"></div>
<div class="cert-window">
  <p class="org">National Institute of Movement Science</p>
  <p class="line" style="top:92px">has conferred upon</p>
  <p class="bold" style="top:138px">Marisa Delgado</p>
  <p class="line" style="top:180px">the certificate of completion for</p>
  <p class="bold" style="top:228px">Fitness Nutrition Specialist (FNS)</p>
  <p class="line" style="top:300px;font-size:23px">with all the honors, rights, privileges and responsibilities pertaining thereto.</p>
  <p class="cert-number">2281904</p>
  <p class="cert-caption">Certificate Number</p>
  <div class="cert-brand"><i></i>NIMS</div>
  <div class="cert-sign" role="img" aria-label="President's signature" style="background:linear-gradient(90deg,transparent,#ddd 30%,#ddd 70%,transparent)"></div>
  <p class="cert-role">President - Summit Fitness &amp; Wellness Group</p>
</div>
<div class="close-btn">
  <svg width="34" height="34" viewBox="0 0 34 34"><path d="M12 12l10 10M22 12l-10 10" stroke="#fff" stroke-width="2"/></svg>
</div>

</body>
</html>
```